Dorvelan Swimming & Athletics Center

We need Business Card for a Athletics center
The logo frome the Uploaded Files ( b card fimal)
Οn one side of card we need the logo of company the Contact and the website:
1. Address:(Limassol, Cyprus 12-14 Stavrinelou str,Ano Trimeni,P.C. 4832)

2.Phone number: (+357) 25-704263

3. Mail: info@dorvelanfit.example

3. Website: www.dorvelanfit.example

Οn the other side of the card we need to write the sport of the company:

1. Artistic Gymnastics
2. Swimming
3. Gym - Fitness
4. Programs
5. Dancing
5.Tennis

From the Uploaded Files you can get the logo.In a logo is behind the black color which can be removed from logo.

Υou can use that color you want.
.
Updates

Industry/Entity Type

Business

Font styles to use
Decorative

Colors
0555a3
ffcf3e
3176b5
0692cd
add136
f04a50
000000
cfcfcf
9d9d9d

Requirements
Should not have
• photos with faces
• photo fro the Website:www.dorvelanfit.example

```html
<!DOCTYPE html>
<html lang="en">
<head>
<meta charset="utf-8">
<title>Dorvelan Swimming &amp; Athletics Center – Business Card</title>
<link href="https://fonts.googleapis.com/css2?family=Roboto:wght@300;400;900&display=swap" rel="stylesheet">
<style>
  :root {
    --backdrop: #2b2b2b;
    --card-dark: #3a3a3c;
    --card-dark-edge: #2e2e30;
    --card-light: #ffffff;
    --accent-blue: #0692cd;
    --accent-blue-deep: #0578ad;
    --brand-gold: #f2a516;
    --text-light: #e6e6e6;
    --text-muted: #cfcfcf;
  }
  * { margin: 0; padding: 0; box-sizing: border-box; }
  html, body {
    width: 1200px; height: 1000px; overflow: hidden;
    background: var(--backdrop);
    font-family: "Roboto", Arial, sans-serif;
  }
  .canvas { position: relative; width: 1200px; height: 1000px; }

  .card {
    position: absolute; top: 150px;
    width: 400px; height: 700px;
    overflow: hidden;
    box-shadow: 0 18px 40px rgba(0,0,0,.55);
  }
  .card--front { left: 160px; background: var(--card-dark); }
  .card--back  { left: 640px; background: linear-gradient(160deg, var(--card-dark) 0%, var(--card-dark-edge) 100%); }

  .card__shapes { position: absolute; inset: 0; width: 100%; height: 100%; }

  /* Front – brand area */
  .brand {
    position: absolute; left: 0; top: 0; width: 400px; height: 360px;
    display: flex; flex-direction: column; align-items: center; justify-content: center;
    gap: 22px;
  }
  .brand__mark {
    width: 62px; height: 62px; border-radius: 50%;
    border: 3px solid var(--brand-gold);
  }
  .brand__name {
    font-weight: 900; font-size: 58px; letter-spacing: 1px;
    color: var(--brand-gold); line-height: 1;
  }

  /* Front – contact */
  .contact {
    position: absolute; left: 0; top: 400px; width: 400px;
    color: var(--text-light); font-weight: 300;
  }
  .contact__pin {
    display: block; margin: 0 auto 10px; width: 26px; height: 26px;
  }
  .contact__address {
    text-align: center; font-size: 17px; line-height: 1.35; letter-spacing: .3px;
  }
  .contact__list { list-style: none; margin: 42px 0 0 60px; }
  .contact__item {
    display: flex; align-items: center; gap: 16px;
    font-size: 18px; letter-spacing: .4px; margin-bottom: 12px;
  }
  .contact__icon { width: 28px; height: 28px; flex: none; }

  /* Back */
  .back__mark {
    position: absolute; left: 172px; top: 70px;
    width: 56px; height: 56px; border-radius: 50%;
    border: 3px solid var(--brand-gold);
  }
  .sports {
    position: absolute; left: 0; top: 330px; width: 400px;
    list-style: none; text-align: center;
    color: var(--text-muted); font-weight: 300;
    font-size: 25px; line-height: 1.3; letter-spacing: 1.5px;
  }
</style>
</head>
<body>
<main class="canvas">

  <!-- Front side: brand and contact -->
  <section class="card card--front" aria-label="Business card front">
    <svg class="card__shapes" viewBox="0 0 400 700" aria-hidden="true">
      <rect x="0" y="0" width="400" height="360" fill="var(--card-light)"/>
      <polygon points="20,0 150,0 150,14 36,30 20,30" fill="var(--accent-blue)" transform="skewX(0)"/>
      <polygon points="0,40 0,0 170,0 150,24 20,40" fill="var(--accent-blue)"/>
      <polygon points="60,360 340,360 340,352 330,320 70,360" fill="var(--accent-blue-deep)"/>
      <polygon points="80,372 320,372 340,332 60,332" fill="var(--accent-blue)"/>
      <polygon points="80,700 320,700 340,664 60,664" fill="var(--accent-blue)"/>
    </svg>

    <div class="brand">
      <span class="brand__mark"></span>
      <span class="brand__name">DORVELAN</span>
    </div>

    <div class="contact">
      <svg class="contact__pin" viewBox="0 0 26 26" aria-hidden="true">
        <circle cx="13" cy="13" r="13" fill="var(--accent-blue)"/>
        <path d="M13 6a4.5 4.5 0 0 0-4.5 4.5C8.5 14 13 19.5 13 19.5s4.5-5.5 4.5-9A4.5 4.5 0 0 0 13 6z" fill="none" stroke="#fff" stroke-width="1.5"/>
        <circle cx="13" cy="10.5" r="1.6" fill="#fff"/>
      </svg>
      <p class="contact__address">Limassol, Cyprus 12-14 Stavrinelou str,<br>Ano Trimeni,P.C. 4832</p>
      <ul class="contact__list">
        <li class="contact__item">
          <svg class="contact__icon" viewBox="0 0 28 28" aria-hidden="true">
            <circle cx="14" cy="14" r="14" fill="var(--accent-blue)"/>
            <path d="M10 8l2.5 0 1 3.5-1.6 1.2a8 8 0 0 0 3.4 3.4l1.2-1.6 3.5 1v2.5a1.5 1.5 0 0 1-1.5 1.5A10 10 0 0 1 8.5 9.5 1.5 1.5 0 0 1 10 8z" fill="none" stroke="#fff" stroke-width="1.4"/>
          </svg>
          <span>(+357) 25-704263</span>
        </li>
        <li class="contact__item">
          <svg class="contact__icon" viewBox="0 0 28 28" aria-hidden="true">
            <circle cx="14" cy="14" r="14" fill="var(--accent-blue)"/>
            <rect x="7.5" y="9.5" width="13" height="9" fill="none" stroke="#fff" stroke-width="1.4"/>
            <path d="M7.5 9.5l6.5 5 6.5-5" fill="none" stroke="#fff" stroke-width="1.4"/>
          </svg>
          <span>info@dorvelanfit.example</span>
        </li>
        <li class="contact__item">
          <svg class="contact__icon" viewBox="0 0 28 28" aria-hidden="true">
            <circle cx="14" cy="14" r="14" fill="var(--accent-blue)"/>
            <circle cx="14" cy="14" r="7" fill="none" stroke="#fff" stroke-width="1.3"/>
            <ellipse cx="14" cy="14" rx="3" ry="7" fill="none" stroke="#fff" stroke-width="1.2"/>
            <path d="M7 14h14M8.5 10.5h11M8.5 17.5h11" stroke="#fff" stroke-width="1.1"/>
          </svg>
          <span>www.dorvelanfit.example</span>
        </li>
      </ul>
    </div>
  </section>

  <!-- Back side: sports offered -->
  <section class="card card--back" aria-label="Business card back">
    <svg class="card__shapes" viewBox="0 0 400 700" aria-hidden="true">
      <polygon points="60,0 340,0 320,30 80,30" fill="var(--accent-blue)"/>
      <rect x="0" y="246" width="400" height="4" fill="var(--accent-blue)"/>
      <polygon points="400,610 400,700 190,700 210,670 390,640" fill="var(--accent-blue)"/>
    </svg>
    <span class="back__mark"></span>
    <ul class="sports">
      <li>ARTISTIC GYMNASTICS</li>
      <li>SWIMING GYM - FITNESS</li>
      <li>PROGRAMS</li>
      <li>DANCING</li>
      <li>TENNIS</li>
    </ul>
  </section>

</main>
</body>
</html>
```